Carry The Tide Home

Business Card design

Target Market(s)

People who require support in the commnity

Industry/Entity Type

Mental Health Support

Contact Information for Business Card

Mental Health Support Rosalind Bratten carrythetidehome@mailvane.com.au 0481 637 592 PO Box 629 Tallowmere QLD 4561

Colors
6B429C
8869AF
B7A5CE
E3DAEB
F3F0F8

Requirements
Must have
• Logo & details listed above
Should not have
• No red or orange

```html
<!DOCTYPE html>
<html lang="en">
<head>
<meta charset="utf-8">
<title>Carry The Tide Home – Business Card</title>
<link href="https://fonts.googleapis.com/css2?family=Arimo:wght@400;700&display=swap" rel="stylesheet">
<style>
  :root {
    --purple-deep: #4B2C7F;
    --purple: #6B429C;
    --purple-mid: #8869AF;
    --lilac: #B7A5CE;
    --mist: #E3DAEB;
    --card: #F3F0F8;
    --ink: #2E2A33;
    --rule: #8A8590;
    --page: #DCD8DE;
  }
  * { margin: 0; padding: 0; box-sizing: border-box; }
  html, body {
    width: 1200px;
    height: 969px;
    overflow: hidden;
    background: var(--page);
    font-family: "Arimo", Arial, sans-serif;
  }
  .business-card {
    position: absolute;
    left: 100px;
    top: 200px;
    width: 1000px;
    height: 568px;
    background: linear-gradient(160deg, #F8F6FB 0%, var(--card) 55%, var(--mist) 100%);
    border-radius: 30px;
    box-shadow: 0 8px 28px rgba(40, 30, 55, 0.18);
  }
  .brand-mark {
    position: absolute;
    left: 133px;
    top: 164px;
    width: 270px;
    height: 270px;
    display: flex;
    align-items: center;
    justify-content: center;
    border-radius: 50%;
    background: linear-gradient(135deg, var(--purple) 0%, var(--purple-mid) 100%);
  }
  .brand-name {
    width: 180px;
    text-align: center;
    color: var(--card);
    font-weight: 700;
    font-size: 24px;
    line-height: 1.2;
    letter-spacing: 1px;
    text-transform: uppercase;
  }
  .divider {
    position: absolute;
    left: 441px;
    top: 177px;
    width: 2px;
    height: 236px;
    background: var(--rule);
  }
  .details {
    position: absolute;
    left: 477px;
    top: 174px;
    color: var(--ink);
  }
  .person-name {
    font-size: 31px;
    font-weight: 700;
    color: var(--purple-deep);
    line-height: 1;
    margin-bottom: 30px;
  }
  .address {
    font-size: 24px;
    line-height: 30px;
    margin-bottom: 14px;
  }
  .contact-line {
    display: flex;
    align-items: center;
    font-size: 24px;
    line-height: 30px;
  }
  .contact-line svg {
    width: 20px;
    height: 20px;
    margin-right: 17px;
    fill: var(--purple-deep);
  }
</style>
</head>
<body>
  <div class="business-card">
    <div class="brand-mark">
      <div class="brand-name">Carry The Tide Home</div>
    </div>

    <div class="divider"></div>

    <div class="details">
      <h1 class="person-name">Rosalind Bratten</h1>
      <p class="address">Mental Health Support<br>PO Box 629<br>Tallowmere QLD 4561</p>
      <p class="contact-line">
        <svg viewBox="0 0 24 24" aria-hidden="true"><path d="M6.6 10.8c1.4 2.8 3.8 5.1 6.6 6.6l2.2-2.2c.3-.3.7-.4 1-.2 1.1.4 2.3.6 3.6.6.6 0 1 .4 1 1V20c0 .6-.4 1-1 1C10.6 21 3 13.4 3 4c0-.6.4-1 1-1h3.5c.6 0 1 .4 1 1 0 1.3.2 2.5.6 3.6.1.3 0 .7-.2 1L6.6 10.8z"/></svg>
        0481 637 592
      </p>
      <p class="contact-line">
        <svg viewBox="0 0 24 24" aria-hidden="true"><path d="M2 6h20v13H2z"/><path d="M3 7l9 6.5L21 7" fill="none" stroke="var(--card)" stroke-width="1.6"/></svg>
        carrythetidehome@mailvane.com.au
      </p>
    </div>
  </div>
</body>
</html>
```